Coffee pack for specialty coffee roasters

Tres Lunas is a premium brand of specialty coffee roasters based in Prague in the Czech Republic.
We sell coffee beans to other coffee shops (wholesale channel) or to final consumers in our own coffee shops (retail)
We are roasting only specialty grade coffee that we source either directly or through specialty coffee merchants.
We have usually 6-8 coffees on our offer list. Each coffee stays with us 2-7 months based on their harvest season.
We pack our coffee for retail purposes in 250g bags that we sell in our cafés, roastery and clients.
We are now changing our bags from side gusset bags with valve closed by tin ties to flat bottom bags with zipper and valve.
We want evolution of our packaging design (not revolution)
Our current bags are decorated by front and back stickers.
New bags will be custom printed with general information and logo (e.g. Manufacturer information, contact, size etc.) and we want to have paper sleeve with customizable information (e.g. Name of the Coffee origin, farmer, taste profile, farm info etc.)

Target Market(s)

Men + woman aged 25-45, socioeconomical group A and B, university educated, interested in quality products, they care about what they drink and eat.

Industry/Entity Type

Coffee Shop

Font styles to use
Other font styles liked:
• Platform regular

Requirements
Must have
• Design of the pack itself and design of paper sleeve that will be excheangable (we need to change name of the coffee and information about it on the paper sleeve)
Nice to have
• nice to have- coffee related design on the bag under the sleeve
Should not have
• any crazy colours (the bag is golden with only black print on it) and sleeve can be colourful but nothing extravagant.

```html
<!DOCTYPE html>
<html lang="cs">
<head>
<meta charset="utf-8">
<title>Tres Lunas – preview 1</title>
<link rel="stylesheet" href="https://fonts.googleapis.com/css2?family=Cabin:wght@400;600;700&family=Open+Sans:wght@400&display=swap">
<style>
  :root {
    --page: #ffffff;
    --ink: #1a1a1a;
    --bag-yellow: #ffd600;
    --cut-line: #3a2a10;
    --tear-line: #b5542a;
    --notch: #e0161b;
    --sleeve-dark: #2f2722;
    --sleeve-mid: #4a3f37;
    --sleeve-map: #2a1214;
    --sleeve-text: #f4efe9;
    --pin-body: #ffffff;
    --pin-bean: #9a6a3a;
  }
  * { margin: 0; padding: 0; box-sizing: border-box; }
  html, body { width: 1200px; height: 1200px; overflow: hidden; background: var(--page); }
  body { position: relative; font-family: "Cabin", sans-serif; color: var(--ink); }

  .sheet-title {
    position: absolute; left: 294px; top: 247px;
    font-family: "Open Sans", sans-serif; font-size: 21px; font-weight: 400; letter-spacing: 0.3px;
  }
  .sheet-title span { margin-left: 18px; }

  .section-label { position: absolute; left: 44px; font-family: "Open Sans", sans-serif; font-size: 15px; }
  .section-label.bag-label { top: 314px; }
  .section-label.sleeve-label { top: 769px; }

  .dieline { position: absolute; overflow: hidden; }
  .dieline svg.guides { position: absolute; inset: 0; }

  /* Bag */
  .bag { left: 46px; top: 339px; width: 736px; height: 388px; background: var(--bag-yellow); }
  .brand-name {
    position: absolute; text-align: center; font-weight: 400; letter-spacing: 0.4px; white-space: nowrap;
  }
  .brand-dot { display: block; margin: 0 auto 4px; border-radius: 50%; border: 2px solid currentColor; }
  .bag-front-brand { left: 130px; top: 122px; width: 240px; font-size: 10px; color: var(--ink); }
  .bag-front-brand .brand-dot { width: 26px; height: 26px; }
  .world-map {
    position: absolute; left: 134px; top: 193px; width: 228px; height: 136px;
    background: var(--ink); border-radius: 40% 45% 35% 40%;
  }
  .bag-back-brand { left: 560px; top: 130px; width: 114px; font-size: 4.5px; color: var(--ink); }
  .bag-back-brand .brand-dot { width: 12px; height: 12px; border-width: 1.2px; margin-bottom: 2px; }
  .bag-back-copy {
    position: absolute; left: 520px; top: 174px; width: 194px;
    text-align: center; font-size: 5.6px; font-weight: 600; line-height: 1.85;
  }
  .bag-back-copy p + p { margin-top: 8px; }
  .bag-back-copy .legal { line-height: 1.5; }
  .net-weight {
    position: absolute; left: 528px; top: 356px; width: 172px;
    display: flex; justify-content: space-between; font-size: 7px; font-weight: 700; white-space: nowrap;
  }

  /* Sleeve */
  .sleeve {
    left: 46px; top: 797px; width: 739px; height: 158px;
    background: radial-gradient(ellipse at 45% 45%, var(--sleeve-mid) 0%, var(--sleeve-dark) 85%);
    color: var(--sleeve-text);
  }
  .origin-map {
    position: absolute; left: 250px; top: 0; width: 120px; height: 152px;
    background: var(--sleeve-map); border-radius: 30% 45% 55% 30% / 20% 35% 65% 40%; opacity: 0.85;
  }
  .origin-pin { position: absolute; left: 297px; top: 40px; width: 15px; height: 24px; }
  .origin-name { position: absolute; left: 160px; top: 19px; font-size: 22px; font-weight: 400; }
  .origin-region { position: absolute; left: 317px; top: 30px; font-size: 7.5px; }
  .coffee-variety { position: absolute; left: 178px; top: 82px; width: 240px; text-align: center; font-size: 10.5px; }
  .taste-notes { position: absolute; left: 178px; top: 104px; width: 240px; text-align: center; font-size: 7.5px; }
  .process-info { position: absolute; left: 178px; top: 134px; width: 240px; text-align: center; font-size: 5px; font-weight: 600; line-height: 1.5; }
  .sleeve-back-brand { left: 563px; top: 12px; width: 114px; font-size: 4.5px; color: var(--sleeve-text); }
  .sleeve-back-brand .brand-dot { width: 12px; height: 12px; border-width: 1.2px; margin-bottom: 2px; }
  .sleeve-back-copy {
    position: absolute; left: 530px; top: 41px; width: 180px;
    text-align: center; font-size: 5.5px; font-weight: 600; line-height: 1.5;
  }
  .roast-date { position: absolute; left: 532px; top: 121px; font-size: 4.5px; font-weight: 600; }
  .roast-date-field { position: absolute; left: 532px; top: 128px; width: 51px; height: 12px; background: #ffffff; }
</style>
</head>
<body>

<h1 class="sheet-title">TRES LUNAS <span>preview 1</span></h1>

<div class="section-label bag-label">Bag</div>
<section class="dieline bag" aria-label="Bag dieline">
  <svg class="guides" width="736" height="388" viewBox="0 0 736 388" aria-hidden="true">
    <g stroke="var(--cut-line)" stroke-width="1" stroke-dasharray="6 5">
      <line x1="130" y1="0" x2="130" y2="388"/>
      <line x1="367" y1="0" x2="367" y2="388"/>
      <line x1="500" y1="0" x2="500" y2="388"/>
    </g>
    <g stroke="var(--tear-line)" stroke-width="0.8" stroke-dasharray="8 4">
      <line x1="130" y1="55" x2="367" y2="55"/>
      <line x1="130" y1="61" x2="367" y2="61"/>
      <line x1="130" y1="67" x2="367" y2="67"/>
      <line x1="500" y1="55" x2="736" y2="55"/>
      <line x1="500" y1="61" x2="736" y2="61"/>
      <line x1="500" y1="67" x2="736" y2="67"/>
    </g>
    <polygon points="130,31 134,35 130,39" fill="var(--notch)"/>
    <polygon points="367,31 363,35 367,39" fill="var(--notch)"/>
  </svg>

  <div class="brand-name bag-front-brand"><span class="brand-dot"></span>TRES LUNAS</div>
  <div class="world-map" role="img" aria-label="Black silhouette map of the world continents"></div>

  <div class="brand-name bag-back-brand"><span class="brand-dot"></span>TRES LUNAS</div>
  <div class="bag-back-copy">
    <p>V ruce držíte čerstvě praženou zrnkovou kávu.<br>
    Pracujeme výhradně s výběrovými jednodruhovými<br>
    arabikami, které získaly 85+ bodů.<br>
    Káva se sbírá na farmách ručně a my navazujeme,<br>
    co nejpřímější, někdy i zcela osobní vazby na farmy.<br>
    To vše, abychom vám mohli přinášet, to nejlepší, co se z<br>
    aktuálních sklizní nabízet dá a podporovat přitom farmáře,<br>
    kteří odvádí na svých farmách velmi tvrdou práci.</p>
    <p>www.tres-lunas.cz @tlroastery FB/prazirnatreslunas</p>
    <p class="legal">Minimální trvanlivost 90 dní od data pražení uvedeného<br>
    na zadní straně obalu.<br>
    Nejlepší chuti dosáhnete do 30 dnů od pražení kávy.<br>
    Výrobce: Tres Lunas s.r.o.,<br>
    Lipová 1204/17, 130 00, Praha 3, ČR</p>
  </div>
  <div class="net-weight"><span>Hmotnost:</span><span>250 g</span></div>
</section>

<div class="section-label sleeve-label">Sleeve</div>
<section class="dieline sleeve" aria-label="Sleeve dieline">
  <div class="origin-map" role="img" aria-label="Dark silhouette map of South America"></div>
  <svg class="guides" width="739" height="158" viewBox="0 0 739 158" aria-hidden="true">
    <g stroke="#d8d0c8" stroke-width="1" stroke-dasharray="6 5">
      <line x1="132" y1="0" x2="132" y2="158"/>
      <line x1="368" y1="0" x2="368" y2="158"/>
      <line x1="501" y1="0" x2="501" y2="158"/>
    </g>
  </svg>

  <svg class="origin-pin" viewBox="0 0 15 24" aria-hidden="true">
    <path d="M7.5 0C3.4 0 0 3.3 0 7.4 0 12.5 7.5 24 7.5 24S15 12.5 15 7.4C15 3.3 11.6 0 7.5 0z" fill="var(--pin-body)"/>
    <ellipse cx="7.5" cy="7.4" rx="3.6" ry="4.3" fill="var(--pin-bean)"/>
  </svg>
  <div class="origin-name">Ekvádor</div>
  <div class="origin-region">Pichincha</div>
  <div class="coffee-variety">100% arabica caturra</div>
  <div class="taste-notes">Lískové ořechy</div>
  <div class="process-info">zpracování: promyté<br>farma: Las Brisas</div>

  <div class="brand-name sleeve-back-brand"><span class="brand-dot"></span>TRES LUNAS</div>
  <div class="sleeve-back-copy">
    Jsme velmi hrdí, že tato káva se prezentuje v naší pražírně již
    počtvrté. V ruce držíte čerstvou sklizeň odrůdy caturra a
    pacas. Tato káva roste ve výšce kolem 1700 metrů nad
    mořem na svazích sopky Pichincha ve specifické biodiverzní
    oblasti mezi pralesem a Andami. Sklizeň této kávy probíhala
    mezi červencem a říjnem 2016 a byla sbírána výhradně
    ručně. Rok od roku také vidíme zlepšující se třídění a balení
    kávy. Kvalita je jednoduše hlavní prioritou farmáře Martína
    Ayaly.
  </div>
  <div class="roast-date">Praženo:</div>
  <div class="roast-date-field"></div>
</section>

</body>
</html>
```